Packaging box for giving wine gifts to customers

I need a nice sturdy elegant box to hold one or two bottles of wine that will give to customers as gifts

Designs look the same

```html
<!DOCTYPE html>
<html lang="en">
<head>
<meta charset="utf-8">
<title>Norvale Wine Gift Box – Flat Design</title>
<link rel="stylesheet" href="https://fonts.googleapis.com/css2?family=Arimo:wght@700&family=Oswald:wght@400;600&family=Great+Vibes&display=swap">
<style>
  :root {
    --page: #f2f2f2;
    --box-black: #0b0b0b;
    --panel-edge: #1c1c1c;
    --cream: #f4eec4;
    --gold-muted: #8d8a6e;
    --white: #ffffff;
    --silver: #cfcfcf;
    --ink: #1a1a1a;
    --wine: #b8323a;
    --gold: #d9a630;
  }
  * { margin: 0; padding: 0; box-sizing: border-box; }
  html, body { width: 1200px; height: 1200px; overflow: hidden; background: var(--page); }
  .canvas { position: relative; width: 1200px; height: 1200px; }

  .panel {
    position: absolute; top: 200px; height: 800px;
    background: var(--box-black); overflow: hidden;
    border: 1px solid var(--panel-edge);
  }
  .side-panel { left: 150px; width: 220px; }
  .front-panel { left: 370px; width: 380px; }
  .bottle-label { left: 810px; width: 260px; border-radius: 4px; }

  .side-title {
    position: absolute; left: 50%; top: 50%;
    transform: translate(-50%, -50%) rotate(-90deg);
    white-space: nowrap;
    font-family: "Oswald", sans-serif; font-weight: 400;
    font-size: 38px; letter-spacing: 22px; color: var(--gold-muted);
  }

  .glass-art {
    position: absolute; left: 50%; top: 100px; transform: translateX(-50%);
    width: 56px; height: 110px;
    background: linear-gradient(180deg, rgba(255,255,255,0.08) 0%, var(--wine) 45%, var(--gold) 100%);
    border-radius: 28px 28px 6px 6px;
  }
  .brand {
    position: absolute; left: 0; right: 0; text-align: center;
    font-family: "Arimo", sans-serif; font-weight: 700; color: var(--white);
  }
  .front-panel .brand { top: 240px; font-size: 56px; letter-spacing: 4px; }
  .tagline {
    position: absolute; left: 0; right: 0; text-align: center; white-space: nowrap;
    font-family: "Oswald", sans-serif; font-weight: 600; color: var(--white);
  }
  .front-panel .tagline { top: 312px; font-size: 14px; }
  .front-panel .rule {
    position: absolute; left: 60px; right: 60px; top: 306px; height: 1px; background: var(--silver);
  }

  .pattern-art {
    position: absolute; left: 0; right: 0; top: 440px; height: 280px;
    background: linear-gradient(180deg, rgba(40,40,40,0) 0%, rgba(40,40,40,0.55) 60%, rgba(40,40,40,0.2) 100%);
  }
  .gift-script {
    position: absolute; left: 0; right: 0; text-align: center;
    font-family: "Great Vibes", cursive; color: var(--cream); line-height: 0.95;
  }
  .gift-script .line1 { display: block; font-size: 96px; }
  .gift-script .line2 { display: block; font-size: 90px; }
  .front-panel .gift-script { top: 470px; }
  .swirl-art {
    position: absolute; left: 50%; top: 680px; transform: translateX(-50%);
    width: 150px; height: 18px; border-radius: 9px;
    background: linear-gradient(90deg, rgba(244,238,196,0) 0%, var(--cream) 50%, rgba(244,238,196,0) 100%);
  }
  .address-band {
    position: absolute; left: 0; right: 0; bottom: 40px; height: 30px;
    background: var(--cream); color: var(--ink);
    font-family: "Arimo", sans-serif; font-weight: 700; font-size: 13px;
    display: flex; align-items: center; justify-content: center;
  }

  .bottle-label .brand { top: 150px; font-size: 40px; letter-spacing: 3px; color: var(--silver); }
  .bottle-label .rule {
    position: absolute; left: 40px; right: 40px; top: 200px; height: 1px; background: var(--silver);
  }
  .bottle-label .tagline { top: 204px; font-size: 10px; color: var(--silver); }
  .chateau-art {
    position: absolute; left: 40px; right: 40px; top: 260px; height: 130px;
    background: linear-gradient(180deg, rgba(244,238,196,0.05) 0%, rgba(244,238,196,0.45) 60%, rgba(244,238,196,0.15) 100%);
  }
  .wine-type {
    position: absolute; left: 0; right: 0; text-align: center;
    font-family: "Arimo", sans-serif; font-weight: 700; color: var(--white);
  }
  .wine-type.kicker { top: 450px; font-size: 18px; letter-spacing: 1px; }
  .wine-type.name { top: 480px; font-size: 52px; line-height: 1.05; color: var(--cream); letter-spacing: 2px; }
  .wine-type.volume { top: 640px; font-size: 18px; }
</style>
</head>
<body>
<main class="canvas">
  <section class="panel side-panel">
    <p class="side-title">WINE FOR YOU</p>
  </section>

  <section class="panel front-panel">
    <div class="glass-art" role="img" aria-label="Illustration of a wine glass filled with red wine"></div>
    <p class="brand">NORVALE</p>
    <div class="rule"></div>
    <p class="tagline">Crafted Quality Is Always Our Promise</p>
    <div class="pattern-art" role="img" aria-label="Faint decorative pattern of wine bottles and glasses"></div>
    <p class="gift-script"><span class="line1">Gifts</span><span class="line2">For You</span></p>
    <div class="swirl-art" role="img" aria-label="Decorative flourish ornament"></div>
    <p class="address-band">Harbor Plaza, 18 Linden Avenue Westbay</p>
  </section>

  <section class="panel bottle-label">
    <p class="brand">NORVALE</p>
    <div class="rule"></div>
    <p class="tagline">Crafted Quality Is Always Our Promise</p>
    <div class="chateau-art" role="img" aria-label="Engraved illustration of a château with vineyard rows"></div>
    <p class="wine-type kicker">MODERN</p>
    <p class="wine-type name">RED<br>WINE</p>
    <p class="wine-type volume">1 Litt</p>
  </section>
</main>
</body>
</html>
```